Attorney Recruiting company needs brochure

Brief Harbor is a company that recruits attorneys for law firms and corporations. We want a brochure that makes the law firms and corporation want to retain us to recruit attorneys when they are hiring. We identify experienced well qualified attorneys. We provide them for direct hire (also knows as permanent placement) and for temporary contract hourly work. We want our colors included: red, black and white. It has to convey professionalism and experience. You can find lots of information about who we are and what we do on our website. www.briefharbor-example.com. The brochure should be in traditional conservative font. Should be easy to read. Attorneys tend to scan brochures to see what we do, they will need read it word for word, so we don't need lots of paragraphs and extraneous text. The brochure should outline easily the services we provide which are very specific. They are outlined on home page of website. You should also include our logo which I will attach in several formats.

Target Market(s)

Attorneys and executives

Industry/Entity Type

Conservative

Requirements
Must have
• logo
colors described above

```html
<!DOCTYPE html>
<html lang="en">
<head>
<meta charset="utf-8">
<title>Brief Harbor – Attorney Recruiting</title>
<link rel="stylesheet" href="https://fonts.googleapis.com/css2?family=Tinos:ital,wght@0,400;0,700;1,400&display=swap">
<style>
  :root {
    --black: #000000;
    --red: #a50000;
    --white: #ffffff;
    --ink: #111111;
    --quote-grey: #9aa3a6;
    --photo-light: #eef1f2;
    --photo-mid: #c9d0d4;
    --photo-dark: #8e979c;
  }
  * { margin: 0; padding: 0; box-sizing: border-box; }
  html, body { width: 1200px; height: 930px; overflow: hidden; background: var(--white); }
  body { font-family: "Tinos", "Times New Roman", serif; color: var(--ink); }
  .brochure-panel { position: relative; width: 1200px; height: 930px; overflow: hidden; background: var(--white); }

  .title-band { position: absolute; left: 0; top: 0; width: 1200px; height: 145px; background: var(--black); }
  .band-title { position: absolute; color: var(--white); font-weight: 700; font-size: 35px; line-height: 36px; letter-spacing: 1px; }
  .band-title--clients { left: 35px; top: 47px; }
  .band-title--process { left: 422px; top: 84px; font-size: 34px; }

  .process-panel { position: absolute; left: 395px; top: 145px; width: 805px; height: 477px; background: var(--red); color: var(--white); }
  .step { position: absolute; width: 350px; }
  .step h3 { font-size: 17px; font-weight: 700; letter-spacing: 0.6px; margin-bottom: 8px; }
  .step p { font-size: 14.6px; line-height: 21.5px; letter-spacing: 0.3px; margin-left: 20px; }
  .step--meet { left: 35px; top: 2px; }
  .step--recruit { left: 35px; top: 245px; }
  .step--screen { left: 465px; top: 2px; }
  .step--hiring { left: 465px; top: 249px; }
  .step--recruit p, .step--hiring p { width: 350px; }

  .workplace-photo { position: absolute; left: 395px; top: 622px; width: 805px; height: 308px;
    background: linear-gradient(90deg, var(--white) 0%, var(--white) 18%, var(--photo-light) 40%, var(--photo-mid) 70%, var(--photo-dark) 100%); }

  .testimonial { position: absolute; font-weight: 700; font-size: 16.4px; line-height: 21px; letter-spacing: 2.1px; color: var(--ink); }
  .testimonial::before { content: "\201C"; position: absolute; left: -30px; top: -14px; font-style: italic; font-weight: 400; font-size: 74px; line-height: 74px; color: var(--quote-grey); letter-spacing: 0; }
  .testimonial cite { display: block; font-style: normal; font-weight: 400; font-size: 11.5px; line-height: 14px; letter-spacing: 1px; margin-top: 6px; }
  .testimonial--specialized { left: 55px; top: 160px; }
  .testimonial--specialized cite { margin-left: 92px; }
  .testimonial--discovery { left: 55px; top: 465px; }
  .testimonial--discovery cite { margin-left: 42px; }
  .testimonial--secured { left: 477px; top: 668px; }
  .testimonial--secured .sign-off { display: block; margin-left: 100px; }
  .testimonial--secured cite { margin-left: 116px; margin-top: 10px; }
</style>
</head>
<body>
<main class="brochure-panel">
  <header class="title-band">
    <h2 class="band-title band-title--clients">What our Clients<br>are Saying:</h2>
    <h2 class="band-title band-title--process">How we Recruit Attorneys for Employers?</h2>
  </header>

  <section class="process-panel">
    <div class="step step--meet">
      <h3>1. Meet the Employer</h3>
      <p>We want to meet with you personally<br>whenever possible to ensure we<br>understand exactly what you need. We<br>want to appreciate both the tangible and<br>intangible aspects of the position.<br>Visiting the office and meeting the<br>people with whom the attorney will<br>work is generally very helpful but<br>not required.</p>
    </div>
    <div class="step step--recruit">
      <h3>2. Recruit Attorneys</h3>
      <p>We are very well networked in the legal<br>community and have reliable referral sources in<br>every area of law and business. We also have an<br>established database of attorneys who are either<br>active or passive job seekers that have<br>confidentially requested us to let them know<br>when the "right position" is available. When<br>needed we also conduct general and targeted<br>advertising.</p>
    </div>
    <div class="step step--screen">
      <h3>3. Screen Attorneys</h3>
      <p>We interview potential candidates with<br>our proven interview system. We<br>conduct reference checks, except<br>where employer prefers to complete<br>reference checks. We confirm that state<br>bar membership is in good standing<br>where applicable.</p>
    </div>
    <div class="step step--hiring">
      <h3>4.Facilitate Interview and Hiring</h3>
      <p>We will present you with resumes and<br>significant commentary from our<br>screening process for the top candidates.<br>You may only need to meet two or three<br>attorney candidates unless you prefer to<br>consider more. We are available to be<br>involved in any aspect of salary and<br>benefit negotiations.</p>
    </div>
  </section>

  <div class="workplace-photo" role="img" aria-label="Smiling professional woman in a bright office with colleagues in the background"></div>

  <blockquote class="testimonial testimonial--specialized">
    We needed an attorney with<br>very specialized legal<br>experience. Brief Harbor<br>understood exactly what we<br>needed and found the perfect<br>addition for our firm. We were<br>able to focus on practicing<br>law while Brief Harbor handled<br>the recruiting process. We will<br>definitely call Brief Harbor<br>next time.”
    <cite>- Managing Shareholder,<br>&nbsp;&nbsp;mid size Orlando specialty firm</cite>
  </blockquote>

  <blockquote class="testimonial testimonial--discovery">
    Our law firm was handling a<br>very complex litigation matter<br>that involved hundreds of boxes<br>of discovery. We were not staffed<br>to get the documents reviewed<br>in a timely manner but did<br>not want to hire additional<br>attorneys. We contacted Brief<br>Harbor and they were able to<br>provide our firm with a team<br>of qualified contract attorneys<br>to handle document review. This<br>permitted our attorneys to handle<br>more substantive matters while<br>still being updated on discovery<br>issues. It was a great solution<br>to an otherwise overwhelming<br>discovery process and we will<br>definitely call Brief Harbor<br>again.”
    <cite>- Partner, large AV rated Orlando law firm</cite>
  </blockquote>

  <blockquote class="testimonial testimonial--secured">
    Thank you for securing an<br>exceptionally qualified attorney<br>for our firm. You clearly<br>understood our goals and<br>objectives and you delivered.<br>We won’t hesitate to contact<br>you next time.
    <span class="sign-off">Thanks so much!”</span>
    <cite>- Managing Shareholder,<br>AV rated national law firm</cite>
  </blockquote>
</main>
</body>
</html>
```